Marketing - Outdoor Vinyl banner, Outdoor Poster, Flyer modifications

Hi, I worked with you in the past and attached flyer designs. It just needs to be tweaked for various prints.
1)Outdoor vinyl banner (4 feet height and 8 feet width) print: Just grand opening pic, logo with name, tagline and call/text us portion.
2)Outdoor Poster (5 feet height and 3 feet width) print: same as above
3) Indoor poster for both horizontal & Vertical prints: Just logo w/ name, tagline, "We are MOVING Next door"
4)Flyer: will give minor modifications to attached flyer designs

```html
<!DOCTYPE html>
<html lang="en">
<head>
<meta charset="utf-8">
<title>Brightway Dental – Grand Opening Banner</title>
<link rel="stylesheet" href="https://fonts.googleapis.com/css2?family=Montserrat:wght@600;700;800&family=Oswald:wght@700&family=Open+Sans:wght@700&family=Roboto+Condensed:wght@400&display=swap">
<style>
  :root {
    --white: #ffffff;
    --slate: #5d7596;
    --slate-dark: #2c405a;
    --navy: #2b3f58;
    --cyan: #0fb0da;
    --cyan-soft: #2ec3d8;
    --ink: #2a3a50;
    --balloon-red: #c9384a;
    --balloon-gold: #f3a41c;
    --balloon-teal: #2ec0d4;
  }
  html, body {
    margin: 0;
    padding: 0;
    width: 1200px;
    height: 600px;
    overflow: hidden;
    background: var(--white);
  }
  .banner {
    position: relative;
    width: 1200px;
    height: 600px;
    overflow: hidden;
    background: var(--white);
    font-family: "Montserrat", Arial, sans-serif;
  }
  .balloons-left {
    position: absolute;
    left: 0; top: 25px;
    width: 150px; height: 270px;
    border-radius: 0 80px 80px 0;
    background: linear-gradient(160deg, rgba(243,164,28,.55), rgba(201,56,74,.45) 45%, rgba(46,192,212,.5));
  }
  .balloons-right {
    position: absolute;
    right: 0; top: 0;
    width: 180px; height: 185px;
    border-radius: 0 0 0 90px;
    background: linear-gradient(200deg, rgba(243,164,28,.55), rgba(201,56,74,.45) 45%, rgba(46,192,212,.5));
  }
  .family-photo {
    position: absolute;
    left: 40px; top: 216px;
    width: 660px; height: 340px;
    border-radius: 30px 30px 0 0;
    background: radial-gradient(ellipse at 50% 45%, #e7c2a6 0%, #c9a58c 30%, #8fb3d8 60%, rgba(230,238,245,.6) 90%);
  }
  .brand {
    position: absolute;
    left: 160px; top: 44px;
    display: flex; align-items: center; gap: 14px;
  }
  .brand-dot {
    width: 40px; height: 40px;
    border-radius: 50%;
    background: var(--cyan);
  }
  .brand-name {
    font-family: "Montserrat", Arial, sans-serif;
    font-weight: 700;
    font-size: 38px;
    letter-spacing: 1px;
    color: var(--cyan);
    text-transform: uppercase;
  }
  .grand-opening {
    position: absolute;
    left: 129px; top: 125px;
    width: 458px; height: 84px;
    border: 5px solid var(--cyan);
    border-radius: 12px;
    background: var(--white);
    display: flex; align-items: center; justify-content: center;
  }
  .grand-opening-inner {
    width: 446px; height: 72px;
    border-radius: 8px;
    background: var(--slate);
    box-shadow: inset 0 0 0 2px var(--white);
    display: flex; align-items: center; justify-content: center;
    font-family: "Oswald", Impact, sans-serif;
    font-weight: 700;
    font-size: 52px;
    letter-spacing: 1px;
    color: var(--white);
  }
  .invite {
    position: absolute;
    left: 716px; top: 52px;
    margin: 0;
    font-weight: 800;
    font-size: 52px;
    line-height: 46.5px;
    letter-spacing: -1.5px;
    color: var(--slate);
    text-transform: uppercase;
  }
  .call-label {
    position: absolute;
    left: 718px; top: 248px;
    margin: 0;
    font-weight: 800;
    font-size: 35px;
    color: var(--navy);
  }
  .phone-bar {
    position: absolute;
    left: 719px; top: 296px;
    width: 398px; height: 54px;
    border-radius: 9px;
    overflow: hidden;
    display: flex;
  }
  .phone-icon {
    width: 76px;
    background: var(--slate-dark);
    display: flex; align-items: center; justify-content: center;
  }
  .phone-number {
    flex: 1;
    background: var(--cyan);
    color: var(--white);
    font-weight: 700;
    font-size: 38px;
    letter-spacing: 1px;
    display: flex; align-items: center; justify-content: center;
  }
  .hours {
    position: absolute;
    left: 717px; top: 356px;
    margin: 0;
    font-family: "Open Sans", Arial, sans-serif;
    font-weight: 700;
    font-size: 23.5px;
    color: var(--slate);
  }
  .disclaimer {
    position: absolute;
    left: 718px; top: 396px;
    margin: 0;
    padding-left: 16px;
    font-family: "Roboto Condensed", Arial Narrow, sans-serif;
    font-size: 17.5px;
    line-height: 23px;
    letter-spacing: -.3px;
    color: var(--ink);
  }
  .disclaimer::before {
    content: "*";
    position: absolute;
    left: 0; top: 0;
    color: var(--cyan);
    font-weight: 700;
  }
  .waves {
    position: absolute;
    left: 0; top: 0;
  }
  .welcome {
    position: absolute;
    right: 38px; top: 544px;
    margin: 0;
    font-weight: 800;
    font-size: 26px;
    letter-spacing: -.3px;
    color: var(--cyan);
  }
</style>
</head>
<body>
<main class="banner">
  <div class="balloons-left" role="img" aria-label="Cluster of red, gold and teal party balloons"></div>
  <div class="balloons-right" role="img" aria-label="Cluster of gold, red and teal party balloons"></div>

  <div class="family-photo" role="img" aria-label="Smiling family of four leaning over a sofa giving thumbs up"></div>

  <svg class="waves" width="1200" height="600" viewBox="0 0 1200 600" aria-hidden="true">
    <path d="M600,520 C650,470 730,470 790,520 L790,600 L600,600 Z" fill="var(--slate)"/>
    <path d="M0,480 C110,440 230,520 360,545 C470,565 580,535 690,515 L1200,462 L1200,600 L0,600 Z" fill="var(--cyan)"/>
    <path d="M0,530 C130,500 250,570 380,582 C500,592 620,560 740,535 L1200,478 L1200,600 L0,600 Z" fill="var(--navy)"/>
    <path d="M0,560 C150,540 260,600 420,600 L0,600 Z" fill="var(--white)" opacity=".0"/>
    <path d="M200,600 C330,575 470,600 600,560" fill="none" stroke="var(--white)" stroke-width="4"/>
  </svg>

  <div class="brand">
    <span class="brand-dot"></span>
    <span class="brand-name">Brightway Dental</span>
  </div>

  <div class="grand-opening">
    <div class="grand-opening-inner">GRAND OPENING</div>
  </div>

  <h1 class="invite">You are<br>invited to<br>opening day<br>party!</h1>

  <p class="call-label">Call or Text Us Now:</p>

  <div class="phone-bar">
    <div class="phone-icon">
      <svg width="40" height="40" viewBox="0 0 40 40" aria-hidden="true">
        <path d="M9,5 L15,5 L17,13 L13,16 C15,21 19,25 24,27 L27,23 L35,25 L35,31 C35,33 33,35 31,35 C18,34 6,22 5,9 C5,7 7,5 9,5 Z" fill="var(--white)"/>
        <path d="M23,7 A11,11 0 0 1 33,17" fill="none" stroke="var(--white)" stroke-width="2.5" stroke-linecap="round"/>
        <path d="M22,12 A6,6 0 0 1 28,18" fill="none" stroke="var(--white)" stroke-width="2.5" stroke-linecap="round"/>
      </svg>
    </div>
    <div class="phone-number">555.014.2290</div>
  </div>

  <p class="hours">Convenient Evening &amp; Saturday Hours</p>

  <p class="disclaimer">Offers cannot be combined and valid for 30 days.<br>Call for details.</p>

  <p class="welcome">New patients are welcome!</p>
</main>
</body>
</html>
```